Talvenridge

We are re-branding the company with a new logo (attached) which I would
like to go on one side of the card, and I have attached a file showing what
the old back side looked like, and I do like the characters that show the
phone, e-mails, etc., I don't like the current arrangement, and I want
something clean, clear and out of the box, as we are an aviation consulting
firm, and we work outside of the box.

```html
<!DOCTYPE html>
<html lang="en">
<head>
<meta charset="utf-8">
<title>Talvenridge – Business Card</title>
<link href="https://fonts.googleapis.com/css2?family=Michroma&family=Exo+2:wght@400;600&display=swap" rel="stylesheet">
<style>
  :root {
    --bg: #a9a9ab;
    --card: #ffffff;
    --brand-red: #b3222b;
    --brand-red-light: #d2353c;
    --charcoal: #444446;
    --ink: #2f2f31;
    --muted: #6b6b6e;
  }
  * { box-sizing: border-box; margin: 0; padding: 0; }
  html, body { width: 1200px; height: 894px; overflow: hidden; }
  body {
    background: var(--bg);
    font-family: "Exo 2", sans-serif;
    color: var(--ink);
    position: relative;
  }
  .card {
    position: absolute;
    left: 240px;
    width: 720px;
    height: 412px;
    background: var(--card);
    box-shadow: 0 6px 18px rgba(0,0,0,.25);
    overflow: hidden;
  }
  .card--front { top: 22px; }
  .card--back { top: 460px; }

  .brand__name {
    font-family: "Michroma", sans-serif;
    color: var(--brand-red);
    letter-spacing: 1px;
    text-transform: uppercase;
    white-space: nowrap;
  }

  /* front */
  .card--front .brand__name {
    position: absolute; left: 50%; top: 50%;
    transform: translate(-50%, -50%);
    font-size: 36px;
  }

  /* back */
  .card--back .brand__name {
    position: absolute; left: 74px; top: 56px;
    font-size: 26px;
  }

  .band { position: absolute; top: 142px; height: 52px; }
  .band--red {
    left: 0; width: 232px;
    background: linear-gradient(90deg, var(--brand-red), var(--brand-red-light) 60%, var(--brand-red));
  }
  .band--charcoal {
    left: 244px; right: 0;
    background: var(--charcoal);
    color: #fff;
    display: flex; align-items: center; justify-content: flex-end;
    padding-right: 40px;
    font-family: "Michroma", sans-serif;
    font-size: 14px; letter-spacing: 1px;
  }

  .person { position: absolute; right: 40px; top: 60px; text-align: right; }
  .person__name { font-family: "Michroma", sans-serif; font-size: 20px; letter-spacing: 1px; }
  .person__role { font-family: "Michroma", sans-serif; font-size: 12px; color: var(--muted); margin-top: 4px; letter-spacing: 1px; }

  .contact-list { list-style: none; position: absolute; font-size: 14px; letter-spacing: .5px; }
  .contact-list li { display: flex; align-items: center; gap: 12px; height: 26px; }
  .contact-list--primary { left: 30px; top: 212px; }
  .contact-list--social { right: 40px; top: 312px; }
  .icon-box {
    width: 18px; height: 18px; background: var(--ink);
    display: flex; align-items: center; justify-content: center; flex: none;
  }
  .icon-box svg { width: 12px; height: 12px; fill: #fff; }
  .icon-box--plain { background: var(--charcoal); }
</style>
</head>
<body>

<section class="card card--front" aria-label="Card front">
  <p class="brand__name">Talvenridge</p>
</section>

<section class="card card--back" aria-label="Card back">
  <p class="brand__name">Talvenridge</p>

  <div class="person">
    <p class="person__name">MARTEN HALE</p>
    <p class="person__role">MANAGER</p>
  </div>

  <div class="band band--red"></div>
  <div class="band band--charcoal">www.talvenridge.com/crew</div>

  <ul class="contact-list contact-list--primary">
    <li>
      <span class="icon-box"><svg viewBox="0 0 12 12"><path d="M6 0a4 4 0 0 0-4 4c0 3 4 8 4 8s4-5 4-8a4 4 0 0 0-4-4zm0 5.5A1.5 1.5 0 1 1 6 2.5a1.5 1.5 0 0 1 0 3z"/></svg></span>
      Harbor Lane 123
    </li>
    <li>
      <span class="icon-box"><svg viewBox="0 0 12 12"><path d="M2.5 0.5 4.5 3 3.5 4.5c.8 1.6 2 2.8 3.6 3.6L8.6 7l2.5 2-1 2.4C5.5 11 1 6.5.6 1.5z"/></svg></span>
      012 555 0147
    </li>
    <li>
      <span class="icon-box"><svg viewBox="0 0 12 12"><path d="M1 2.5h10v7H1zM1.8 3.3 6 6.5l4.2-3.2v.9L6 7.4 1.8 4.2z"/></svg></span>
      mhale@talvenridge.com
    </li>
  </ul>

  <ul class="contact-list contact-list--social">
    <li><span class="icon-box icon-box--plain"></span>www.talvenridge.com</li>
    <li><span class="icon-box icon-box--plain"></span>www.social-one.net</li>
    <li><span class="icon-box icon-box--plain"></span>www.social-two.net</li>
  </ul>
</section>

</body>
</html>
```